Triathlon coaching company website design

A website is needed for a coaching company called StrideMosaic. The company provides coaching services to triathletes and other endurance athletes. This includes 1:1 coaching, individualized training plan development, race preparation, and access to guidance and advice on all aspects of developing and maintaining a healthy lifestyle. The design should appeal to all levels of athletes, but be professional in appearance. The tone of the site should be in keeping with the company tagline: Endurance. Resilience. Achievement.

Target Market(s)

All levels of triathletes - beginners to professionals

Industry/Entity Type

It Company

Coding

Coded - Design and coding required

Number of Pages Required

1 page

Colors

Designer to choose colors to be used in the design.

Requirements
Must have
• Pages that should be included must cover: Introductory (Home), description in detail of what we do, description of the main coach (bio) and others types of expert advisors who can be available, link to contact the company, race reports for coaches and athletes that can be regularly updated, links to other sites of potential interest (e.g. other triathlon sites or my facebook page), twitter feed, sign up for email updates. Ability to add other links and pages in future months (e.g. shared calendar access to book meetings, credit card functionality, testimonials)
Should not have
• Not loud or down market feel - target market will largely be highly educated and reasonably affluent

```html
<!DOCTYPE html>
<html lang="en">
<head>
<meta charset="utf-8">
<title>StrideMosaic — Endurance. Resilience. Achievement.</title>
<link href="https://fonts.googleapis.com/css2?family=Roboto:wght@300;400;500;700;900&display=swap" rel="stylesheet">
<style>
:root{
  --red:#b3282d;
  --red-dark:#9c1f24;
  --ink:#222222;
  --charcoal:#1f1f1f;
  --band:#2c2c2c;
  --grey-text:#555555;
  --light:#f1f1f1;
  --white:#ffffff;
}
*{box-sizing:border-box;margin:0;padding:0}
html,body{width:1200px;height:3147px;overflow:hidden}
body{font-family:'Roboto',Arial,sans-serif;color:var(--ink);background:var(--white);position:relative}

/* Hero */
.hero{position:absolute;top:0;left:0;width:1200px;height:581px;
  background:linear-gradient(180deg,#6f7679 0%,#8a8f8c 35%,#5d5a55 60%,#3a3633 100%);overflow:hidden}
.hero-photo{position:absolute;inset:0;
  background:radial-gradient(ellipse 380px 300px at 330px 300px,rgba(90,80,70,.55),transparent 70%),
  linear-gradient(100deg,transparent 55%,rgba(70,95,60,.45) 75%,rgba(40,55,35,.5) 100%)}
.site-nav{position:absolute;top:0;left:0;width:1200px;height:90px}
.brand{position:absolute;left:162px;top:30px;color:var(--red)}
.brand-name{font-size:34px;font-weight:700;line-height:1;display:flex;align-items:center;gap:8px}
.brand-name::before{content:"";width:14px;height:14px;border-radius:50%;background:var(--red)}
.brand-tag{font-size:10px;color:var(--white);letter-spacing:.5px;margin-top:4px;text-transform:uppercase}
.menu{position:absolute;right:162px;top:44px;display:flex;gap:27px;list-style:none}
.menu li{color:var(--white);font-size:12px;font-weight:500;text-transform:uppercase;letter-spacing:.3px}
.hero-copy{position:absolute;top:268px;left:0;width:1200px;text-align:center;color:var(--white)}
.hero-copy h1{font-size:30px;font-weight:700;letter-spacing:.5px}
.hero-copy p{font-size:34px;font-weight:300;margin-top:2px}
.btn-pill{display:inline-block;margin-top:32px;background:var(--red);color:var(--white);
  font-size:17px;font-weight:700;padding:14px 34px;border-radius:26px}

/* Welcome */
.welcome{position:absolute;top:581px;left:0;width:1200px;height:485px;background:var(--red);overflow:hidden}
.welcome-photo{position:absolute;right:0;top:0;width:640px;height:485px;
  background:radial-gradient(ellipse 200px 260px at 400px 240px,rgba(60,30,30,.55),transparent 75%),
  linear-gradient(90deg,rgba(179,40,45,0) 0%,rgba(120,28,32,.35) 100%)}
.welcome-copy{position:absolute;left:162px;top:58px;width:470px;color:var(--white)}
.welcome-copy h2{font-size:33px;font-weight:900;text-transform:uppercase;line-height:1;white-space:nowrap}
.welcome-copy .tagline{font-size:17px;letter-spacing:3.6px;font-weight:300;margin-top:8px;text-transform:uppercase;white-space:nowrap}
.welcome-copy .body{border-left:3px solid var(--white);padding-left:16px;margin-top:20px;font-size:11px;line-height:1.5}
.welcome-copy .body p+p{margin-top:12px}
.btn-outline{display:inline-block;margin-top:28px;margin-left:24px;border:2px solid var(--white);color:var(--white);
  font-size:15px;font-weight:500;padding:13px 18px;text-transform:uppercase}

/* Services */
.services{position:absolute;top:1116px;left:162px;width:877px;height:332px;display:flex;gap:10px}
.card{width:240px;height:332px;background:var(--white);border:1px solid #dcdcdc;text-align:center}
.card-photo{height:170px}
.card h3{font-size:15px;font-weight:700;margin-top:20px;text-transform:uppercase}
.card h3::after{content:"";display:block;width:34px;height:2px;background:var(--red);margin:8px auto 0}
.card p{font-size:11px;color:var(--grey-text);line-height:1.55;padding:16px 24px 0}
.services-panel{width:127px;height:332px;background:var(--charcoal);color:var(--white);padding:18px 12px}
.services-panel small{font-size:13px;display:block}
.services-panel strong{font-size:22px;font-weight:700;display:block;line-height:1}
.services-panel strong::after{content:"";display:block;width:30px;height:2px;background:var(--red);margin-top:6px}
.services-panel p{font-size:10px;line-height:1.55;margin-top:12px;color:#ddd}
.arrows{display:flex;gap:6px;margin-top:24px}
.arrows span{width:28px;height:28px;border:1px solid var(--white);display:flex;align-items:center;justify-content:center}

/* Approach */
.approach{position:absolute;top:1490px;left:0;width:1200px;text-align:center}
.section-title{font-size:36px;font-weight:700;color:var(--ink);text-transform:uppercase}
.stars{display:flex;align-items:center;justify-content:center;gap:6px;margin-top:10px}
.stars i{display:block;width:110px;height:1px;background:#ccc}
.approach p{width:770px;margin:28px auto 0;font-size:11.5px;line-height:1.7;color:var(--grey-text)}

/* Lifestyle band */
.lifestyle{position:absolute;top:1752px;left:0;width:1200px;height:220px;
  background:linear-gradient(90deg,#262626,#363636 50%,#242424)}
.lifestyle-box{position:absolute;left:162px;top:38px;width:877px;height:144px;border:2px solid #aaa;
  background:rgba(0,0,0,.35);display:flex;align-items:center;justify-content:center;text-align:center;
  color:var(--white);font-size:35px;font-weight:700;line-height:1.2;text-transform:uppercase}

/* About */
.about{position:absolute;top:2010px;left:0;width:1200px}
.about .section-title{text-align:center}
.about .underline{width:40px;height:3px;background:var(--red);margin:10px auto 0}
.about-panel{position:absolute;left:390px;top:84px;width:649px;height:310px;background:var(--red);color:var(--white);padding:38px 30px 0 245px}
.about-panel h3{font-size:21px;font-weight:700;text-transform:uppercase}
.about-panel h3::after{content:"";display:block;width:34px;height:2px;background:var(--white);margin-top:8px}
.about-panel p{font-size:10.5px;line-height:1.6;margin-top:14px;text-align:justify}
.coach-frame{position:absolute;left:162px;top:126px;width:438px;height:304px;background:#ddd;border:4px solid #cfcfcf}
.coach-photo{position:absolute;inset:0;background:linear-gradient(135deg,#1c1c1c,#3a3a3a 60%,#151515)}
.coach-caption{position:absolute;left:0;right:0;bottom:30px;height:40px;background:rgba(240,240,240,.92);
  display:flex;align-items:center;justify-content:center;font-size:15px;font-weight:500;text-transform:uppercase}

/* Consulting */
.consulting{position:absolute;top:2528px;left:0;width:1200px;height:267px;background:linear-gradient(90deg,#f4f4f4,#e6e6e6 60%,#efefef)}
.consulting h2{position:absolute;left:162px;top:57px;font-size:27px;font-weight:700;text-transform:uppercase}
.consulting p{position:absolute;left:162px;top:92px;font-size:12px;color:var(--grey-text)}
.btn-dark{position:absolute;left:766px;top:59px;width:273px;height:46px;background:var(--charcoal);color:var(--white);
  font-size:15px;font-weight:700;display:flex;align-items:center;justify-content:center;gap:10px;text-transform:uppercase}

/* Footer */
.footer{position:absolute;top:2795px;left:0;width:1200px;height:352px;background:var(--charcoal);color:var(--white);text-align:center}
.newsletter{position:absolute;top:2704px;left:162px;width:877px;height:174px;background:var(--red);color:var(--white);text-align:center;padding-top:22px}
.newsletter h2{font-size:25px;font-weight:700;text-transform:uppercase}
.newsletter p{font-size:12px;margin-top:6px}
.signup{display:flex;justify-content:center;margin-top:18px}
.signup span{width:354px;height:40px;background:var(--white);color:#999;font-size:11px;text-align:left;padding:13px 12px}
.signup b{width:110px;height:40px;background:var(--charcoal);font-weight:400;font-size:15px;display:flex;align-items:center;justify-content:center}
.footer h2{position:absolute;top:110px;width:100%;font-size:35px;font-weight:500}
.social{position:absolute;top:170px;width:100%;display:flex;justify-content:center;gap:12px}
.social span{width:34px;height:34px;border:1px solid #aaa;border-radius:50%}
.foot-links{position:absolute;top:260px;width:100%;display:flex;justify-content:center;gap:22px;list-style:none;font-size:10px;color:#bbb;text-transform:uppercase}
.foot-links li+li::before{content:"|";margin-right:22px;color:#777}
.copyright{position:absolute;top:297px;width:100%;font-size:10px;color:#999}
</style>
</head>
<body>

<header class="hero">
  <div class="hero-photo" role="img" aria-label="Runner in starting position on an outdoor athletics track under a cloudy sky"></div>
  <nav class="site-nav">
    <div class="brand">
      <div class="brand-name">StrideMosaic</div>
      <div class="brand-tag">Endurance. Resilience. Achievement</div>
    </div>
    <ul class="menu">
      <li>Home</li><li>Our Services</li><li>Bio</li><li>Expert Advisors</li><li>Race Reports</li><li>Contact Us</li>
    </ul>
  </nav>
  <div class="hero-copy">
    <h1>STRIDEMOSAIC</h1>
    <p>Endurance. Resilience. Achievement</p>
    <span class="btn-pill">CONTACT US</span>
  </div>
</header>

<section class="welcome">
  <div class="welcome-photo" role="img" aria-label="Athlete lifting dumbbells in a gym"></div>
  <div class="welcome-copy">
    <h2>Welcome to StrideMosaic</h2>
    <div class="tagline">Endurance. Resilience. Achievement</div>
    <div class="body">
      <p>Lorem Ipsum is simply dummy text of the printing and typesetting industry. Lorem Ipsum has been the industry's standard dummy text ever since the 1500s, when an unknown printer took a galley of type and scrambled it to make a type specimen book. It has survived not only five centuries, but also the leap into electronic typesetting, remaining essentially unchanged. It was popularised in the 1960s with the release of Lettersheet sheets containing Lorem Ipsum passages, and more recently with desktop publishing software like PageComposer including versions of Lorem Ipsum.</p>
      <p>Lorem Ipsum is simply dummy text of the printing and typesetting industry. Lorem Ipsum has a galley of type and scrambled it to make a type specimen book. It has survived not only five centuries, but also the leap into electronic typesetting, remaining essentially unchanged. It was ages, and more recently with desktop publishing software like PageComposer including versions of Lorem Ipsum.</p>
    </div>
    <span class="btn-outline">Start your coaching online</span>
  </div>
</section>

<section class="services">
  <article class="card">
    <div class="card-photo" role="img" aria-label="Basketball team huddled with their coach" style="background:linear-gradient(135deg,#2d3b6a,#8a7d78 60%,#cfc6c0)"></div>
    <h3>1:1 Coaching</h3>
    <p>Lorem Ipsum is simply dummy text Ipsum has been the industry's standard scrambled it to make a type specimen ries, Lorem Ipsum.</p>
  </article>
  <article class="card">
    <div class="card-photo" role="img" aria-label="Runners training together at sunset" style="background:linear-gradient(180deg,#2b4f9a,#d6803a 65%,#6a4a3a)"></div>
    <h3>Training Plan Development</h3>
    <p>Lorem Ipsum is simply dummy text Ipsum has been the industry's standard scrambled it to make a type specimen ries, Lorem Ipsum.</p>
  </article>
  <article class="card">
    <div class="card-photo" role="img" aria-label="Coach in conversation with a client" style="background:linear-gradient(135deg,#7a4e4a,#c9a48f 50%,#d8d2cc)"></div>
    <h3>Lifestyle Coaching</h3>
    <p>Lorem Ipsum is simply dummy text Ipsum has been the industry's standard scrambled it to make a type specimen ries, Lorem Ipsum.</p>
  </article>
  <aside class="services-panel">
    <small>OUR</small>
    <strong>SERVICES</strong>
    <p>Plans built around you, with steady support from first session to finish line, adapting as your goals, fitness and busy week change across every training block.</p>
    <div class="arrows">
      <span><svg width="10" height="10" viewBox="0 0 10 10"><path d="M7 1 3 5l4 4" fill="none" stroke="#fff" stroke-width="2"/></svg></span>
      <span><svg width="10" height="10" viewBox="0 0 10 10"><path d="M3 1l4 4-4 4" fill="none" stroke="#fff" stroke-width="2"/></svg></span>
    </div>
  </aside>
</section>

<section class="approach">
  <h2 class="section-title">Our Approach</h2>
  <div class="stars"><i></i>
    <svg width="40" height="10" viewBox="0 0 40 10"><g fill="#333"><path d="M5 0l1.5 3.2 3.5.4-2.6 2.4.7 3.5L5 7.7 1.9 9.5l.7-3.5L0 3.6l3.5-.4z"/><path d="M35 0l1.5 3.2 3.5.4-2.6 2.4.7 3.5L35 7.7l-3.1 1.8.7-3.5L30 3.6l3.5-.4z"/></g><path fill="#b3282d" d="M20 0l1.5 3.2 3.5.4-2.6 2.4.7 3.5L20 7.7l-3.1 1.8.7-3.5L15 3.6l3.5-.4z"/></svg>
  <i></i></div>
  <p>At StrideMosaic we believe that everyone has a unique set of circumstances, motivations and abilities that need to be taken into consideration in developing their program. Defining success is personal, as is the path to achieving that success. Every person has their own goals; for some it is about health and wellness, for others the focus is lifestyle, and in other cases specific competitive goals are the target. So we focus on understanding you as an individual athlete in the context of your wider life - your goals, your training history, your physiology and psychology as well as other aspects of your life. The foundation of any program should be based on objective data and facts, overlaid with personal experience and circumstance. Given the right approach we strive to help athletes of all types and levels improve endurance, increase their resilience in the face of challenges, and develop a powerful sense of achievement. Endurance, Resilience, Achievement are the watch-words of the StrideMosaic brand.</p>
</section>

<section class="lifestyle">
  <div class="lifestyle-box">Developing and maintaining a healthy<br>lifestyle</div>
</section>

<section class="about">
  <h2 class="section-title">About Me</h2>
  <div class="underline"></div>
  <div class="about-panel">
    <h3>Daniel Ashcombe</h3>
    <p>Triathlon is my passion which, in the past, coexisted with my day job as a management consultant - so I absolutely understand the challenges of fitting triathlon into a busy work, family and social life. I started competing in endurance sports in my teens as a rower, ultimately competing for Great Britain at the World Championships, and have continued as an endurance athlete throughout my life. My first triathlon was an Olympic distance event in Japan in 2001, which sparked my interest in the complexities and rewards of multi-sport and long distance racing. I continued to compete after moving to the U.S., and since then I have competed in many triathlon and running events, including 14 full distance 140.6 and as many 70.3 races, including three times World Championships and two times 70.3 World Championships. I am a certified ECA and NTF L1 coach.</p>
  </div>
  <div class="coach-frame">
    <div class="coach-photo" role="img" aria-label="Portrait of the head coach in a gym"></div>
    <div class="coach-caption">Daniel Ashcombe</div>
  </div>
</section>

<section class="consulting">
  <h2>Consulting Service</h2>
  <p>Lorem Ipsum is simply dummy text of the printing and typesetting industry Lorem Ipsum.</p>
  <span class="btn-dark">Get free consultation
    <svg width="10" height="14" viewBox="0 0 10 14"><path d="M2 1l6 6-6 6" fill="none" stroke="#fff" stroke-width="2.5"/></svg></span>
</section>

<footer class="footer">
  <h2>Join the conversation</h2>
  <div class="social"><span></span><span></span><span></span><span></span><span></span></div>
  <ul class="foot-links">
    <li>Home</li><li>Our Services</li><li>Bio</li><li>Expert Advisors</li><li>Race Reports</li><li>Contact Us</li>
  </ul>
  <div class="copyright">StrideMosaic © 2018 All rights reserved. Terms of use and Privacy Policy</div>
</footer>

<section class="newsletter">
  <h2>Newsletter</h2>
  <p>Enter your email adress for getting updates</p>
  <div class="signup"><span>Enter your email id</span><b>Subscribe</b></div>
</section>

</body>
</html>
```